Business cards for education company

We need a business card design for a relatively new company based in Queensland and operating across Australia. We resell diploma level education courses which include Business, Management, Finance, Community Services & Government courses. We offer over 20 different courses.
The target market is for anyone 16 years of age and older. There is no age limit.

We would like to see the design use the color blue and silver. The final design should communicate professionalism and a bright future.

We sell education but are also promoting the career they see themselves in 2-3 years in the future

Our company logo is attached.

Target Market(s)

We target all age groups above 16 years of age. The main target market would be people aged between 17-35.

We focus on those people who cannot make it into University or do not want to commit the time to a full degree.

Industry/Entity Type

Education

Requirements
Must have
• Professional
Company logo
website
Contact details:

Please use the following example:

Lionel Parfitt
Senior Education Consultant
0417 386 591
Lionel.parfitt@brightwaylearninghub.com.au
www.brightwaylearninghub.com.au

```html
<!DOCTYPE html>
<html lang="en">
<head>
<meta charset="utf-8">
<title>Brightway Learning Hub – Business Card</title>
<link rel="stylesheet" href="https://fonts.googleapis.com/css2?family=Tenor+Sans&family=Marcellus&display=swap">
<style>
  :root {
    --bg: #2a2a2c;
    --card-grey: #58575c;
    --panel-dark: #1b1b1d;
    --brand-blue: #2f80d1;
    --ink: #19191b;
    --stripe-black: #0d0d0e;
  }
  * { margin: 0; padding: 0; box-sizing: border-box; }
  html, body { width: 1200px; height: 900px; overflow: hidden; background: var(--bg); }
  .stage { position: relative; width: 1200px; height: 900px; }

  .card {
    position: absolute; left: 270px; width: 660px; height: 377px;
    background: var(--card-grey); overflow: hidden;
    box-shadow: 0 10px 30px rgba(0,0,0,.45);
  }
  .card--back { top: 48px; }
  .card--front { top: 470px; }

  /* back */
  .back-disc {
    position: absolute; left: 50%; top: 50%; width: 330px; height: 330px;
    margin: -165px 0 0 -165px; border-radius: 50%; background: var(--panel-dark);
    display: flex; align-items: center; justify-content: center;
  }
  .brand { display: flex; align-items: center; gap: 12px; }
  .brand-dot { width: 22px; height: 22px; border-radius: 50%; background: var(--brand-blue); flex: none; }
  .brand-name {
    font-family: "Tenor Sans", sans-serif; color: var(--brand-blue);
    font-size: 22px; letter-spacing: 1px; text-transform: uppercase; line-height: 1.1;
  }
  .back-disc .brand-name { font-size: 24px; }

  /* front */
  .tab {
    position: absolute; left: 0; background: var(--panel-dark);
    border-radius: 0 22px 22px 0;
  }
  .tab--brand { top: 30px; width: 360px; height: 82px; display: flex; align-items: center; padding-left: 34px; }
  .tab--name { top: 122px; width: 470px; height: 96px; }
  .person {
    position: absolute; left: 34px; top: 140px;
    font-family: "Tenor Sans", sans-serif; color: var(--brand-blue);
  }
  .person-name { font-size: 40px; letter-spacing: 3px; font-variant: small-caps; line-height: 1; }
  .person-role { font-size: 20px; letter-spacing: .5px; margin-top: 6px; }

  .contacts {
    position: absolute; left: 34px; top: 252px; list-style: none;
    font-family: "Marcellus", serif; font-size: 18px; color: var(--ink);
  }
  .contacts li { display: flex; align-items: center; gap: 12px; height: 34px; }
  .contacts svg { width: 20px; height: 20px; flex: none; }

  .stripes { position: absolute; right: 0; top: 0; width: 200px; height: 200px; }
</style>
</head>
<body>
<main class="stage">

  <section class="card card--back" aria-label="Card back">
    <div class="back-disc">
      <div class="brand">
        <span class="brand-dot"></span>
        <span class="brand-name">Brightway<br>Learning Hub</span>
      </div>
    </div>
  </section>

  <section class="card card--front" aria-label="Card front">
    <svg class="stripes" viewBox="0 0 200 200" aria-hidden="true">
      <line x1="60" y1="-5" x2="140" y2="175" stroke="var(--brand-blue)" stroke-width="7"/>
      <line x1="75" y1="-5" x2="155" y2="175" stroke="var(--stripe-black)" stroke-width="6"/>
      <line x1="90" y1="-5" x2="170" y2="175" stroke="var(--brand-blue)" stroke-width="7"/>
    </svg>

    <div class="tab tab--brand">
      <div class="brand">
        <span class="brand-dot"></span>
        <span class="brand-name">Brightway Learning Hub</span>
      </div>
    </div>
    <div class="tab tab--name"></div>

    <div class="person">
      <p class="person-name">Lionel Parfitt</p>
      <p class="person-role">Senior Education Consultant</p>
    </div>

    <ul class="contacts">
      <li>
        <svg viewBox="0 0 20 20" aria-hidden="true"><rect x="1" y="1" width="18" height="18" rx="3" fill="var(--ink)"/><path d="M6 5c1 0 1.5 2 1.5 2.5S6.5 9 7 10s2 2.5 3 3 1.5-.5 2-1 2.5.5 2.5 1.5S13 15 12 15 5 11 5 6.5 5.5 5 6 5z" fill="var(--card-grey)"/></svg>
        <span>0417 386 591</span>
      </li>
      <li>
        <svg viewBox="0 0 20 20" aria-hidden="true"><rect x="1" y="4" width="18" height="12" fill="none" stroke="var(--ink)" stroke-width="1.6"/><path d="M1 4l9 7 9-7" fill="none" stroke="var(--ink)" stroke-width="1.6"/></svg>
        <span>Lionel.parfitt@brightwaylearninghub.com.au</span>
      </li>
      <li>
        <svg viewBox="0 0 20 20" aria-hidden="true"><circle cx="10" cy="10" r="8" fill="none" stroke="var(--ink)" stroke-width="1.5"/><ellipse cx="10" cy="10" rx="3.5" ry="8" fill="none" stroke="var(--ink)" stroke-width="1.2"/><line x1="2" y1="10" x2="18" y2="10" stroke="var(--ink)" stroke-width="1.2"/></svg>
        <span>www.brightwaylearninghub.com.au</span>
      </li>
    </ul>
  </section>

</main>
</body>
</html>
```